Best in class cloud software provider for retailers needs a new business card design to reflect prod

We are a software company based out of Chicago selling into retailers. We have a new website and marketing collateral that support our new product designs. We are obsessed with simplicity, ease of use, and having a really powerful product set. We have two products as noted on our website - www.brolvane.com - one is a retail task management product and the other is a Help Ticketing product.

At Brolvane we are passionate about creating the best Retail Task Management system in the industry. We bring more than 20 years of retail operations, Workforce Management and Retail Task experience and have a set of web and mobile software features that no one else has. Brolvane enables you to plan and distribute work throughout your organization and ensure it gets done.

We need a new business card design that reflects our new branding, message and approach.

I've attached a few documents that help support what we are building and how our colors look.

There may be additional future work if this goes well.

Thanks,
Mark

President

Target Market(s)

We sell into retailers and are a software company

Industry/Entity Type

Software

Contact Information for Business Card

The card must have

Name
title
address
tele
email
Brolvane logo (someplace)

So for example

It would have for me

Mark Dorsett
President
48 West Harlow Ave. Suite 310
Chicago, IL 60687
3125550187
mdorsett@brolvane.com

Requirements
Must have
• We need to cards for 5 different people - same design different names etc
Nice to have
• should reflect our colors and product and website - be creative - ease of use, simplicity, and power is what the product is about - but we are very forward Brolvane and hear all the time that our product is gorgeous. The font should be consistent with our website, and marketing one pager included
Should not have
• Strange or unfamiliar colors or fonts...

```html
<!DOCTYPE html>
<html lang="en">
<head>
<meta charset="utf-8">
<title>Brolvane Business Card</title>
<link rel="stylesheet" href="https://fonts.googleapis.com/css2?family=Oswald:wght@400;500;600&display=swap">
<style>
  :root {
    --backdrop: #d6dadb;
    --paper: #f4f4f2;
    --teal: #2a95a4;
    --ink: #161616;
    --brand-red: #d8401f;
  }
  * { margin: 0; padding: 0; box-sizing: border-box; }
  html, body {
    width: 1200px;
    height: 745px;
    overflow: hidden;
    background: var(--backdrop);
  }
  .stage {
    width: 1200px;
    height: 745px;
    display: flex;
    align-items: center;
    justify-content: center;
    gap: 80px;
  }
  .card {
    position: relative;
    width: 345px;
    height: 600px;
    overflow: hidden;
    box-shadow: 0 6px 18px rgba(0, 0, 0, 0.12);
  }

  /* Front */
  .card-front {
    background: var(--paper);
    font-family: "Oswald", sans-serif;
  }
  .identity {
    position: absolute;
    top: 78px;
    left: 34px;
    right: 20px;
  }
  .person-name {
    color: var(--teal);
    font-weight: 500;
    font-size: 44px;
    line-height: 1;
    letter-spacing: 3px;
    text-transform: uppercase;
  }
  .person-title {
    color: var(--ink);
    font-weight: 600;
    font-size: 30px;
    line-height: 1;
    letter-spacing: 2.5px;
    text-transform: uppercase;
    margin-top: 2px;
    margin-left: 96px;
  }
  .contact {
    position: absolute;
    top: 262px;
    left: 0;
    right: 0;
    text-align: center;
    color: var(--ink);
    font-weight: 400;
    font-size: 15px;
    line-height: 1.65;
    letter-spacing: 1.6px;
    text-transform: uppercase;
  }
  .contact .gap { margin-top: 12px; }
  .brand-front {
    position: absolute;
    left: 22px;
    bottom: 22px;
    color: var(--brand-red);
    font-weight: 600;
    font-size: 74px;
    line-height: 1;
    letter-spacing: 0.5px;
  }

  /* Back */
  .card-back {
    background: var(--teal);
    font-family: "Oswald", sans-serif;
  }
  .brand-band {
    position: absolute;
    left: 0;
    right: 0;
    top: 228px;
    height: 118px;
    background: var(--paper);
    display: flex;
    align-items: center;
    justify-content: center;
  }
  .brand-back {
    color: var(--brand-red);
    font-weight: 600;
    font-size: 74px;
    line-height: 1;
    letter-spacing: 0.5px;
  }
</style>
</head>
<body>
  <main class="stage">
    <section class="card card-front" aria-label="Business card front">
      <div class="identity">
        <h1 class="person-name">Mark Dorsett</h1>
        <p class="person-title">President</p>
      </div>
      <div class="contact">
        <p>mdorsett@brolvane.com</p>
        <p>3125550187</p>
        <p class="gap">48 West Harlow Ave. Suite 310</p>
        <p>Chicago, IL 60687</p>
      </div>
      <div class="brand-front">Brolvane</div>
    </section>

    <section class="card card-back" aria-label="Business card back">
      <div class="brand-band">
        <div class="brand-back">Brolvane</div>
      </div>
    </section>
  </main>
</body>
</html>
```